Business Card - Professional Minimalist - Double sided

We appreciate minimalist logo/web/collateral designs that allow design to tell a story. We want to relay a professional image/approach but throwing in a splash of modern when we’re able so long as it’s not distracting. Think 75% classic corporate, 25% modern. Open to black or white design, not sure which might look the best.

Target Market(s)

Senior executives or related government affairs contacts within the agriculture, energy, and defense industries (i.e., potential clients) but located outside of Washington, DC. Most potential clients based in DC with be familiar with both of us and our shared history.

Industry/Entity Type

Consulting

Contact Information for Business Card

Name: Derek M. Holloway
Title: Co-Founder & Partner
Address: 418 Linwood Terrace NE | Suite 2260 | Washington, D.C. 20017
Phone: (202) 555-0148
Email: Derek@BrimleyHolloway.example

Font styles to use
Serif

Colors

Designer to choose only greyscale colors for use in the design.

Requirements
Must have
• Name: Derek M. Holloway
Phone: (202) 555-0148

```html
<!DOCTYPE html>
<html lang="en">
<head>
<meta charset="utf-8">
<title>Brimley Holloway Group – Business Card</title>
<link rel="stylesheet" href="https://fonts.googleapis.com/css2?family=Marcellus&display=swap">
<style>
  :root {
    --backdrop: #b9b9b9;
    --card-white: #fbfbfb;
    --card-black: #141414;
    --ink: #2a2a2a;
    --ink-soft: #555555;
    --rule: #8a8a8a;
    --silver: #c9c9c9;
    --silver-dim: #7a7a7a;
  }
  * { box-sizing: border-box; margin: 0; padding: 0; }
  html, body {
    width: 1200px; height: 675px; overflow: hidden;
    background: var(--backdrop);
    font-family: "Marcellus", serif;
  }
  .stage {
    position: relative; width: 1200px; height: 675px;
    display: flex; align-items: center; justify-content: center; gap: 60px;
  }
  .card {
    position: relative; width: 500px; height: 286px;
    border-radius: 16px; overflow: hidden;
  }
  .card--front { background: var(--card-white); color: var(--ink); }
  .card--back { background: var(--card-black); color: var(--silver); }

  /* front */
  .brand { position: absolute; left: 34px; top: 38px; display: flex; align-items: flex-start; gap: 12px; }
  .brand__square { width: 34px; height: 34px; border: 2px solid var(--ink-soft); margin-top: 2px; }
  .brand__name { font-size: 24px; letter-spacing: 1.5px; line-height: 1; color: var(--ink-soft); }
  .brand__rule { display: block; height: 1px; background: var(--rule); margin: 8px 0 4px; }
  .brand__sub { display: block; text-align: right; font-size: 10px; letter-spacing: 5px; color: var(--ink-soft); }

  .person__name {
    position: absolute; right: 28px; top: 166px;
    font-size: 22px; line-height: 26px; letter-spacing: 0.5px;
    color: var(--ink); text-transform: uppercase; white-space: nowrap;
  }
  .person__role {
    position: absolute; right: 28px; top: 206px;
    font-size: 11px; line-height: 13px; color: var(--ink-soft);
  }

  .contact { position: absolute; left: 34px; right: 28px; top: 196px; font-size: 12px; line-height: 14px; color: var(--ink-soft); }
  .contact__title { display: flex; align-items: center; gap: 6px; }
  .contact__title::after { content: ""; flex: 1 1 auto; height: 1px; background: var(--rule); }
  .contact__line { display: flex; align-items: center; gap: 6px; margin-top: 5px; white-space: nowrap; }
  .contact__line svg { width: 10px; height: 10px; fill: var(--ink-soft); flex: none; }
  .contact__pair { display: flex; gap: 26px; }

  /* back */
  .mark { position: absolute; inset: 0; display: flex; flex-direction: column; align-items: center; justify-content: center; }
  .mark__square { width: 34px; height: 34px; border: 2px solid var(--silver); }
  .mark__rule { width: 1px; height: 40px; background: var(--silver-dim); margin: 10px 0 14px; }
  .mark__name { font-size: 28px; letter-spacing: 2px; line-height: 1; }
  .mark__sub { font-size: 11px; letter-spacing: 6px; margin-top: 8px; }
</style>
</head>
<body>
<main class="stage">
  <section class="card card--front" aria-label="Card front">
    <div class="brand">
      <div class="brand__square"></div>
      <div>
        <div class="brand__name">BRIMLEY HOLLOWAY</div>
        <span class="brand__rule"></span>
        <span class="brand__sub">GROUP</span>
      </div>
    </div>

    <div class="person__name">Derek M. Holloway</div>

    <div class="contact">
      <div class="contact__title">Co-Founder &amp; Partner</div>
      <div class="contact__line">
        <svg viewBox="0 0 10 10" aria-hidden="true"><path d="M5 0a3.5 3.5 0 0 0-3.5 3.5C1.5 6 5 10 5 10s3.5-4 3.5-6.5A3.5 3.5 0 0 0 5 0zm0 5a1.4 1.4 0 1 1 0-2.8A1.4 1.4 0 0 1 5 5z"/></svg>
        418 Linwood Terrace NE | Suite 2260 | Washington, D.C. 20017
      </div>
      <div class="contact__pair">
        <div class="contact__line">
          <svg viewBox="0 0 10 10" aria-hidden="true"><path d="M2 0.5l2 2-1 1.2c.6 1.3 1.6 2.3 2.8 2.9L7 5.5l2 2-1.3 1.8C4.3 9 1 5.7.6 2.1z"/></svg>
          (202) 555-0148
        </div>
        <div class="contact__line">
          <svg viewBox="0 0 10 10" aria-hidden="true"><path d="M0 2h10v6H0zm1 1v.3l4 2.5 4-2.5V3z"/></svg>
          Derek@BrimleyHolloway.example
        </div>
      </div>
    </div>

    <div class="person__role">Owner</div>
  </section>

  <section class="card card--back" aria-label="Card back">
    <div class="mark">
      <div class="mark__square"></div>
      <div class="mark__rule"></div>
      <div class="mark__name">BRIMLEY HOLLOWAY</div>
      <div class="mark__sub">GROUP</div>
    </div>
  </section>
</main>
</body>
</html>
```